Eye catching Stationary Design

Healthcare consultant firm looking for stationary design ( letterhead, envelope and business cards) That’s professional, classy and eye catching . The design should incorporate the logo and the colors of the logo in its design. You can see the logo on our website at www harbor key advisors. com.

```html
<!DOCTYPE html>
<html lang="en">
<head>
<meta charset="utf-8">
<title>Harbor Key Advisors – Business Cards</title>
<link rel="stylesheet" href="https://fonts.googleapis.com/css2?family=Cinzel:wght@500&family=Montserrat:wght@500;700&display=swap">
<style>
  :root {
    --backdrop: #1e1e1e;
    --paper: #ffffff;
    --sky: #2ba6d6;
    --navy: #0d5aa8;
    --ink: #1f2328;
    --mark-blue: #2a8fd0;
  }
  * { margin: 0; padding: 0; box-sizing: border-box; }
  html, body { width: 1200px; height: 900px; overflow: hidden; }
  body {
    background: var(--backdrop);
    font-family: "Montserrat", sans-serif;
    position: relative;
  }
  .card {
    position: absolute;
    left: 290px;
    width: 620px;
    height: 354px;
    background: var(--paper);
    overflow: hidden;
    box-shadow: 0 10px 30px rgba(0,0,0,.5);
  }
  .card--front { top: 60px; }
  .card--back { top: 486px; }
  .card__shape { position: absolute; inset: 0; width: 100%; height: 100%; }

  .brand {
    position: absolute;
    display: flex;
    align-items: center;
    gap: 10px;
  }
  .brand__dot {
    width: 22px; height: 22px;
    border-radius: 50%;
    background: var(--mark-blue);
    flex: none;
  }
  .brand__name {
    font-family: "Cinzel", serif;
    font-weight: 500;
    color: var(--ink);
    letter-spacing: .04em;
    white-space: nowrap;
  }
  .card--front .brand { left: 150px; top: 120px; }
  .card--front .brand__name { font-size: 21px; }
  .card--back .brand { left: 34px; top: 182px; }
  .card--back .brand__name { font-size: 14px; }

  .front-contact {
    position: absolute;
    right: 60px;
    bottom: 52px;
    color: var(--paper);
    font-size: 15px;
    font-weight: 500;
    text-align: right;
    line-height: 1.7;
  }
  .front-contact__web { display: flex; align-items: center; justify-content: flex-end; gap: 8px; }

  .profile { position: absolute; left: 378px; top: 58px; }
  .profile__name {
    color: var(--paper);
    font-weight: 700;
    font-size: 24px;
    letter-spacing: .02em;
    text-transform: uppercase;
    white-space: nowrap;
  }
  .profile__role {
    color: var(--navy);
    font-weight: 500;
    font-size: 18px;
    text-transform: uppercase;
    margin-top: 2px;
  }
  .contacts {
    position: absolute;
    left: 378px;
    right: 16px;
    top: 176px;
    list-style: none;
    color: var(--ink);
    font-size: 13px;
    font-weight: 500;
    line-height: 1.35;
  }
  .contacts li { display: flex; align-items: flex-start; gap: 8px; margin-bottom: 8px; white-space: nowrap; }
  .contact-icon {
    width: 17px; height: 17px;
    border-radius: 50%;
    background: var(--paper);
    flex: none;
    display: flex; align-items: center; justify-content: center;
  }
  .contact-icon svg { width: 11px; height: 11px; }
</style>
</head>
<body>

<section class="card card--front">
  <svg class="card__shape" viewBox="0 0 620 354" preserveAspectRatio="none">
    <path d="M0 292 Q 340 262 620 78 L620 354 L0 354 Z" fill="var(--navy)"/>
    <path d="M0 300 Q 345 278 620 102 L620 354 L0 354 Z" fill="var(--sky)"/>
  </svg>
  <div class="brand">
    <span class="brand__dot"></span>
    <span class="brand__name">Harbor Key Advisors LLC</span>
  </div>
  <div class="front-contact">
    <div class="front-contact__web">
      <span class="contact-icon">
        <svg viewBox="0 0 12 12" fill="none" stroke="var(--navy)" stroke-width="1.2"><circle cx="6" cy="6" r="5"/><path d="M1 6h10M6 1c-2.5 3-2.5 7 0 10M6 1c2.5 3 2.5 7 0 10"/></svg>
      </span>
      <span>harborkeyadvisors.com</span>
    </div>
    <div>info@harborkeyadvisors.com</div>
  </div>
</section>

<section class="card card--back">
  <svg class="card__shape" viewBox="0 0 620 354" preserveAspectRatio="none">
    <path d="M190 0 Q 380 150 330 354 L620 354 L620 0 Z" fill="var(--navy)"/>
    <path d="M215 0 Q 400 160 346 354 L620 354 L620 0 Z" fill="var(--sky)"/>
  </svg>
  <div class="brand">
    <span class="brand__dot"></span>
    <span class="brand__name">Harbor Key Advisors LLC</span>
  </div>
  <div class="profile">
    <h1 class="profile__name">Marcus Hale</h1>
    <p class="profile__role">Director</p>
  </div>
  <ul class="contacts">
    <li>
      <span class="contact-icon">
        <svg viewBox="0 0 12 12" fill="var(--navy)"><path d="M2.5 1h2l1 3-1.3 1a6 6 0 0 0 2.8 2.8l1-1.3 3 1v2a1 1 0 0 1-1 1A9.5 9.5 0 0 1 1.5 2a1 1 0 0 1 1-1z"/></svg>
      </span>
      <span>(555) 014-0172</span>
    </li>
    <li>
      <span class="contact-icon">
        <svg viewBox="0 0 12 12" fill="none" stroke="var(--navy)" stroke-width="1.2"><circle cx="6" cy="6" r="5"/><path d="M1 6h10M6 1c-2.5 3-2.5 7 0 10M6 1c2.5 3 2.5 7 0 10"/></svg>
      </span>
      <span>info@harborkeyadvisors.com</span>
    </li>
    <li>
      <span class="contact-icon">
        <svg viewBox="0 0 12 12" fill="var(--navy)"><path d="M6 0.5a4 4 0 0 1 4 4c0 3-4 7-4 7s-4-4-4-7a4 4 0 0 1 4-4zm0 2.3a1.7 1.7 0 1 0 0 3.4 1.7 1.7 0 0 0 0-3.4z"/></svg>
      </span>
      <span>118 Linden St Suite 40,<br>Portland, ME 04101, USA</span>
    </li>
  </ul>
</section>

</body>
</html>
```